Brochure for new townhouse development

We need a brochure created for our new townhouse development that we can provide to potential purchasers for off-the-plan sales.

2 similar examples are attached.

Brochure content is to include the text as per the attached word document (brochure text) and as follows:
Cover
The Development
At a Glance
The Location - also to include the 2d map and aerial photo (have included screenshot of map and aerial photo as a placeholder, to be replaced in the final version)
Plans - include 3d floor plans, I have included a sample 3d floor plan as a placeholder, this is to be replaced in the final version.
Finishes - as per word document attached, and colour samples attached
Specifications - as per word document attached
Subdivision plan - I have attached a plan which can be used as a placeholder, the final version will be ready next week and is to be replaced in the final version
Landscape plan - as per attached
Rental assessment - as per attached
Stake your Claim

Renders of the building are attached and can be used throughout the brochure.

There is no company name or logo to include.

We have other upcoming developments and would look to reuse the winning brochure so there is future and ongoing work.

```html
<!DOCTYPE html>
<html lang="en">
<head>
<meta charset="utf-8">
<title>Contents</title>
<link rel="preconnect" href="https://fonts.googleapis.com">
<link href="https://fonts.googleapis.com/css2?family=Lato:wght@900&family=PT+Sans:wght@400&display=swap" rel="stylesheet">
<style>
  :root {
    --bg-base: #ecdfc1;
    --bg-glow: #f8f2e6;
    --title: #ffffff;
    --ink: #8e6a3d;
    --marker: #93693a;
    --wood-light: #e8d5b3;
    --wood-mid: #d9bf96;
  }
  html, body {
    margin: 0;
    padding: 0;
    overflow: hidden;
  }
  .page {
    position: relative;
    width: 1200px;
    height: 849px;
    overflow: hidden;
    background:
      radial-gradient(ellipse 460px 380px at 930px 440px, var(--bg-glow) 0%, rgba(248,242,230,0) 80%),
      var(--bg-base);
  }
  .contents-title {
    position: absolute;
    left: 141px;
    top: 168px;
    margin: 0;
    font-family: "Lato", sans-serif;
    font-weight: 900;
    font-size: 39px;
    line-height: 1.2;
    letter-spacing: 0.5px;
    color: var(--title);
  }
  .contents-list {
    position: absolute;
    left: 140px;
    top: 232px;
    margin: 0;
    padding: 0;
    list-style: none;
    width: 250px;
  }
  .contents-item {
    display: flex;
    align-items: center;
    height: 38.3px;
    font-family: "PT Sans", sans-serif;
    font-size: 16px;
    letter-spacing: 1px;
    color: var(--ink);
    white-space: nowrap;
  }
  .marker {
    flex: none;
    width: 10px;
    height: 10px;
    margin-right: 14px;
  }
  .marker path { fill: var(--marker); }
  .label { flex: none; word-spacing: 4px; }
  .leader {
    flex: 1;
    overflow: hidden;
    letter-spacing: 1.2px;
  }
  .dining-render {
    position: absolute;
    left: 554px;
    top: 366px;
    width: 646px;
    height: 483px;
    background: linear-gradient(180deg, var(--wood-light) 0%, var(--wood-mid) 100%);
  }
</style>
</head>
<body>
  <main class="page">
    <h1 class="contents-title">CONTENTS</h1>
    <ul class="contents-list">
      <li class="contents-item"><svg class="marker" viewBox="0 0 11 11"><path d="M0 0H11V11L5.5 7.5L0 11Z"/></svg><span class="label">THE DEVELOPMENT</span><span class="leader">..................................</span></li>
      <li class="contents-item"><svg class="marker" viewBox="0 0 11 11"><path d="M0 0H11V11L5.5 7.5L0 11Z"/></svg><span class="label">AT A GLANCE</span><span class="leader">..................................</span></li>
      <li class="contents-item"><svg class="marker" viewBox="0 0 11 11"><path d="M0 0H11V11L5.5 7.5L0 11Z"/></svg><span class="label">THE LOCATION</span><span class="leader">..................................</span></li>
      <li class="contents-item"><svg class="marker" viewBox="0 0 11 11"><path d="M0 0H11V11L5.5 7.5L0 11Z"/></svg><span class="label">PLANS</span><span class="leader">..................................</span></li>
      <li class="contents-item"><svg class="marker" viewBox="0 0 11 11"><path d="M0 0H11V11L5.5 7.5L0 11Z"/></svg><span class="label">FINISHES</span><span class="leader">..................................</span></li>
      <li class="contents-item"><svg class="marker" viewBox="0 0 11 11"><path d="M0 0H11V11L5.5 7.5L0 11Z"/></svg><span class="label">SPECIFICATIONS&nbsp;&nbsp;</span><span class="leader">..................................</span></li>
      <li class="contents-item"><svg class="marker" viewBox="0 0 11 11"><path d="M0 0H11V11L5.5 7.5L0 11Z"/></svg><span class="label">SUBDIVISION PLAN</span><span class="leader">..................................</span></li>
      <li class="contents-item"><svg class="marker" viewBox="0 0 11 11"><path d="M0 0H11V11L5.5 7.5L0 11Z"/></svg><span class="label">LANDSCAPE PLAN&nbsp;&nbsp;</span><span class="leader">..................................</span></li>
      <li class="contents-item"><svg class="marker" viewBox="0 0 11 11"><path d="M0 0H11V11L5.5 7.5L0 11Z"/></svg><span class="label">RENTAL ASSESSMENT</span><span class="leader">..................................</span></li>
      <li class="contents-item"><svg class="marker" viewBox="0 0 11 11"><path d="M0 0H11V11L5.5 7.5L0 11Z"/></svg><span class="label">STAKE YOUR CLAIM</span><span class="leader">..................................</span></li>
    </ul>
    <div class="dining-render" role="img" aria-label="Render of a round timber dining table with four wooden chairs, a vase of pink and white peonies and a black tea set"></div>
  </main>
</body>
</html>
```